Create the design of Sitepelican (in photoshop or similar)

*edit* What we wanna see is a sketch of a first page, and then in the end 5 page designs, but the main page will be the big tasks other pages are just basically pop-ups or form. *edit*

We need a web design for our new startup Sitepelican in turn will be providing web pages to smaller business. So the purpose of the page is to clearly showcase the message in a web 3.0 fashion, good design looks but function should always be the main focus.Further more we are looking for a long term relationship with a good designer / design company that can help us design the future web sites for our customers as well.

We need you to understand web, not just design. You need to be up to date with how web looks and works, and how to make it as simple and easy to use as possible for the customer and at the same time good looking.

Please look at the PDF for full description of the project.

Colors and layout are free to choose, but we really like the kind of layout that forkglider.com has so feel free to be inspired by them.

We want all of the pages design, but the main/landing page will be the big part, the rest are small pages that will use the same design frame as the main page.

PS. We just want the design in photoshop or illustrator format, the website will then be built in page tidal by page tidal experts (let us know if you/company also possess this knowledge)

Target Market(s)

Small to medium sized business, mostly owner/entrepreneur driven companies.

Industry/Entity Type

Business

Font styles to use
Other font styles liked:
• Helvetica for the win

Requirements
Must have
• Great and simple design, a child should be able to understand the message and also enjoy reading it. Should be a funny website while still being professional, i.e. see postbadger.com for example.

```html
<!DOCTYPE html>
<html lang="en">
<head>
<meta charset="utf-8">
<title>Sitepelican – most convenient web ever</title>
<link href="https://fonts.googleapis.com/css2?family=Open+Sans:wght@400;600&family=Roboto:wght@300;400&display=swap" rel="stylesheet">
<style>
:root{
  --teal:#1bb99a;
  --teal-dark:#15967c;
  --text:#555555;
  --heading:#5a5a5a;
  --light-bg:#f7f7f7;
  --footer:#0d0d0d;
  --white:#ffffff;
  --border:#e2e2e2;
}
*{margin:0;padding:0;box-sizing:border-box}
html,body{width:1200px;height:2209px;overflow:hidden}
body{position:relative;background:var(--white);font-family:"Roboto",Helvetica,Arial,sans-serif;color:var(--text)}
.abs{position:absolute}

/* header */
.site-header{left:0;top:0;width:1200px;height:147px;background:var(--teal)}
.brand-mark{left:87px;top:30px;width:90px;height:90px;border:3px solid var(--white);border-radius:50%}
.brand-name{left:200px;top:34px;font-family:"Open Sans",sans-serif;font-size:40px;color:var(--white);letter-spacing:-.5px}
.brand-tagline{left:201px;top:88px;font-family:"Open Sans",sans-serif;font-size:16px;font-weight:600;color:var(--white)}
.main-nav{top:70px;font-family:"Open Sans",sans-serif;font-size:17px;color:var(--white)}

/* hero */
.hero{left:0;top:147px;width:1200px;height:408px;
  background:linear-gradient(90deg,#efd9cc 0%,#eef0f2 20%,#f1f2f3 50%,#e8eaec 75%,#c7ccd2 100%)}
.hero-title{left:0;top:268px;width:1200px;text-align:center;font-weight:300;font-size:40px;color:var(--heading)}
.hero-title span{color:var(--teal);font-weight:400}
.hero-list{left:238px;list-style:none;font-size:20px;font-weight:300;color:#777}
.hero-list li::before{content:"";position:absolute;left:0;top:10px;width:10px;height:10px;border-radius:50%;background:var(--teal)}
.hero-list li{position:relative;padding-left:22px;height:36px}

/* offers */
.offer-title{top:628px;width:473px;text-align:center;font-weight:300;font-size:40px;color:var(--heading)}
.offer-image{top:707px;width:473px;height:312px}
.offer-text{width:473px;text-align:center;font-size:16px;line-height:40px;color:#555}
.icon-inline{display:inline-block;vertical-align:middle;margin:0 8px}
.price-button{left:234px;top:1155px;width:199px;height:53px;background:var(--teal);border:3px solid var(--white);outline:2px solid var(--teal);color:var(--white);font-family:"Open Sans",sans-serif;font-weight:600;font-size:16px;text-align:center;line-height:47px}
.partner-name{left:638px;top:1162px;width:473px;text-align:center;font-weight:300;font-size:32px;color:var(--heading)}

/* calculator */
.calculator{left:0;top:1290px;width:1200px;height:643px;background:var(--light-bg)}
.calc-title{left:0;top:1350px;width:1200px;text-align:center;font-weight:300;font-size:40px;line-height:57px;color:var(--heading)}
.calc-illustration{left:125px;top:1490px;width:351px;height:370px;
  background:radial-gradient(ellipse at 55% 45%,#d8dcdf 0%,#c0c5c9 35%,#e4564c 60%,#fbfbfb 80%)}
.field{left:637px;width:417px;height:58px;background:var(--white);border:1px solid var(--border);border-radius:3px;padding-left:18px;font-size:16px;line-height:56px;color:#999}
.field-select::after{content:"";position:absolute;right:18px;top:25px;border:7px solid transparent;border-top-color:#888}
.calc-button{left:637px;top:1796px;width:417px;height:55px;background:var(--teal);border-bottom:3px solid var(--teal-dark);border-radius:3px;color:var(--white);font-family:"Open Sans",sans-serif;font-weight:600;font-size:23px;text-align:center;line-height:52px}

/* call to action */
.cta-band{left:0;top:1933px;width:1200px;height:144px;background:var(--teal)}
.cta-text{left:129px;top:1987px;font-family:"Open Sans",sans-serif;font-size:33px;color:var(--white)}
.cta-button{left:663px;top:1977px;width:411px;height:62px;background:var(--teal-dark);color:var(--white);font-family:"Open Sans",sans-serif;font-size:31px;text-align:center;line-height:62px}

/* footer */
.site-footer{left:0;top:2077px;width:1200px;height:132px;background:var(--footer)}
.footer-links{left:120px;top:2115px;font-family:Arial,Helvetica,sans-serif;font-size:14px;color:var(--white)}
.footer-copy{left:120px;top:2149px;font-family:Arial,Helvetica,sans-serif;font-size:14px;color:var(--white)}
.social{top:2126px;width:37px;height:37px}
</style>
</head>
<body>

<header class="abs site-header"></header>
<div class="abs brand-mark"></div>
<div class="abs brand-name">sitepelican.se</div>
<div class="abs brand-tagline">most convenient web ever</div>
<nav>
  <a class="abs main-nav" style="left:571px">How it works</a>
  <a class="abs main-nav" style="left:710px">About us</a>
  <a class="abs main-nav" style="left:818px">Contact us</a>
  <a class="abs main-nav" style="left:937px">FAQ</a>
  <a class="abs main-nav" style="left:1012px">Privacy Policy</a>
</nav>

<section class="abs hero" role="img" aria-label="Blurred photo of a bright office workspace"></section>
<h1 class="abs hero-title">What is Sitepelican? <span>?</span></h1>
<ul class="abs hero-list" style="top:340px">
  <li>Your website on subscription autopilot with free unlimited support and updates.</li>
  <li>Delivered by professionals</li>
</ul>

<h2 class="abs offer-title" style="left:87px">What does it cost?</h2>
<div class="abs offer-image" style="left:87px;background:linear-gradient(135deg,#c9cfbf,#8d9a83 50%,#d5d9cc)" role="img" aria-label="Pile of banknotes"></div>
<p class="abs offer-text" style="left:87px;top:1056px">About the same as 1
  <svg class="icon-inline" width="34" height="26" viewBox="0 0 34 26"><rect x="2" y="2" width="22" height="18" rx="2" fill="#1bb99a"/><path d="M24 6h4a4 4 0 0 1 0 8h-4" fill="none" stroke="#1bb99a" stroke-width="3"/><rect x="0" y="22" width="30" height="3" fill="#1bb99a"/></svg>
  a day and guaranteed less than a<br>really good night out with the gang
  <svg class="icon-inline" width="18" height="28" viewBox="0 0 18 28"><path d="M2 2h14c0 8-3 12-7 12S2 10 2 2z" fill="#1bb99a"/><rect x="8" y="14" width="2" height="10" fill="#1bb99a"/><rect x="3" y="24" width="12" height="2" fill="#1bb99a"/></svg>
</p>
<a class="abs price-button">See price details here</a>

<h2 class="abs offer-title" style="left:638px">If you are unhappy?</h2>
<div class="abs offer-image" style="left:638px;background:radial-gradient(circle at 58% 58%,#e0201c 0%,#e0201c 22%,#f6df0a 24%,#f2d400 100%)" role="img" aria-label="Crowd of yellow balls with one red ball"></div>
<p class="abs offer-text" style="left:638px;top:1056px">Cancel the same day, we will refund you all your money and<br>buy you a year of Tunewave subscription</p>
<div class="abs partner-name">Tunewave</div>

<section class="abs calculator"></section>
<h2 class="abs calc-title">Test your website now! How many more customers could<br>you get every month?</h2>
<div class="abs calc-illustration" role="img" aria-label="Cartoon rocket launching with flame"></div>
<div class="abs field" style="top:1509px">Visitors per month</div>
<div class="abs field" style="top:1579px">Current conversion rate in %</div>
<div class="abs field" style="top:1651px">Improve conversion rate, 1 - 3%</div>
<div class="abs field field-select" style="top:1723px">SEK</div>
<a class="abs calc-button">Calculate</a>

<section class="abs cta-band"></section>
<div class="abs cta-text">See prices and details for</div>
<a class="abs cta-button">Most convenient web ever</a>

<footer class="abs site-footer"></footer>
<div class="abs footer-links">Terms and Conditions | Privacy Policy | FAQs | Contact</div>
<div class="abs footer-copy">Copyrights 2013. All Rights Reserved.</div>
<span class="abs social" style="left:917px;background:#3b5998"></span>
<span class="abs social" style="left:966px;background:#2aa9e0"></span>
<span class="abs social" style="left:1016px;background:#f26522"></span>
<span class="abs social" style="left:1064px;background:#d62b2b"></span>

</body>
</html>
```